Draft Beer System Services Sales Sheet

Wanting a sales sheet (leave behind) to match the glycol chiller maintenance sales sheet you created earlier this year (.pdf attached) for our company. I will upload a sketch with dialogue. I will also upload some relevant images. Can't wait to see this come together.

Target Market(s)

Bars, Brewery Tap Rooms, Restaurants, Sporting Venues

Industry/Entity Type

Draft Beer and Brewery Services

Font styles to use
Serif

Requirements
Must have
• Similar theme as previous sales sheet
Nice to have
• Images that seem relevant

```html
<!DOCTYPE html>
<html lang="en">
<head>
<meta charset="utf-8">
<title>Draft Beer System Services – Tapline Pro</title>
<link rel="stylesheet" href="https://fonts.googleapis.com/css2?family=Barlow+Condensed:wght@700;800&family=Open+Sans:wght@400;500&display=swap">
<style>
  :root{
    --gold:#e8a934;
    --gold-text:#f0ad2a;
    --charcoal:#2b2b2b;
    --ink:#262626;
    --white:#ffffff;
    --steel:#c4c4c4;
    --steel-dark:#8d8d8d;
  }
  *{margin:0;padding:0;box-sizing:border-box}
  html,body{width:1200px;height:826px;overflow:hidden;background:var(--white)}
  .sheet{position:relative;width:1200px;height:826px;font-family:"Open Sans",sans-serif;color:var(--white)}
  .backdrop{position:absolute;left:0;top:0}
  .tap-tower-photo{position:absolute;left:16px;top:8px;width:336px;height:186px;border-radius:6px;
    background:linear-gradient(160deg,#9a9a9a,#e2e2e2 45%,#6e6e6e)}
  .guarantee-badge{position:absolute;left:358px;top:50px;width:124px;height:124px;border-radius:50%;background:var(--ink)}
  .brand-mark{position:absolute;left:990px;top:70px;display:flex;align-items:center;gap:8px;
    font-family:"Open Sans",sans-serif;font-weight:500;font-size:24px;color:var(--ink)}
  .brand-mark .dot{width:22px;height:22px;border-radius:50%;background:var(--ink)}
  .title{position:absolute;left:503px;top:56px;font-family:"Barlow Condensed",sans-serif;font-weight:800;line-height:1}
  .title .line-1{display:block;font-size:66px;color:var(--white);letter-spacing:1px}
  .title .line-2{display:block;font-size:72px;color:var(--ink);margin-top:4px;letter-spacing:.3px}
  .service{position:absolute;left:0;width:1200px}
  .service-icon{position:absolute;left:74px;width:76px;height:70px;border-radius:6px;background:rgba(232,169,52,.28)}
  .service-rule{position:absolute;left:172px;width:4px;background:var(--gold-text)}
  .service-name{position:absolute;left:252px;font-size:38px;font-weight:500;line-height:46px;color:var(--gold-text)}
  .service-points{position:absolute;left:506px;list-style:none;font-size:16.5px;letter-spacing:1px;line-height:20px}
  .service-points li{position:relative;padding-left:24px}
  .service-points li::before{content:"";position:absolute;left:0;top:9px;width:4px;height:4px;border-radius:50%;background:var(--white)}
  .tap-handles-photo{position:absolute;left:772px;top:600px;width:406px;height:226px;border-radius:8px 0 0 0;
    background:linear-gradient(180deg,#3a3a3a 0%,#7a4a2a 40%,#c98a4c 70%,#8a5a2e 100%)}
  .strengths{position:absolute;left:70px;top:742px;list-style:none;font-size:17px;line-height:24px;color:var(--gold-text)}
  .strengths li::before{content:"-";display:inline-block;width:25px}
  .contact{position:absolute;left:408px;top:746px;font-size:13px;letter-spacing:1.5px;line-height:17px;font-style:normal}
  .contact .company{font-weight:500;letter-spacing:1.8px}
  .contact .row{display:flex;align-items:center;gap:6px}
  .contact svg{width:11px;height:11px;fill:var(--gold-text)}
</style>
</head>
<body>
<main class="sheet">
  <svg class="backdrop" width="1200" height="826" viewBox="0 0 1200 826" aria-hidden="true">
    <rect x="16" y="0" width="1162" height="826" fill="var(--gold)"/>
    <path d="M16 150 Q600 262 1178 238 L1178 648 Q600 632 16 680 Z" fill="var(--charcoal)"/>
    <path d="M16 148 Q600 260 1178 236" fill="none" stroke="var(--steel)" stroke-width="7"/>
    <path d="M16 682 Q600 634 1178 650" fill="none" stroke="var(--steel-dark)" stroke-width="4"/>
    <rect x="16" y="728" width="1162" height="98" fill="var(--charcoal)"/>
  </svg>

  <div class="tap-tower-photo" role="img" aria-label="Photo of a chrome six-tap draft beer tower"></div>

  <div class="guarantee-badge" role="img" aria-label="Satisfaction guarantee badge"></div>

  <div class="brand-mark"><span class="dot"></span>Tapline Pro</div>

  <h1 class="title"><span class="line-1">DRAFT BEER</span><span class="line-2">SYSTEM SERVICES</span></h1>

  <section class="service" style="top:264px">
    <div class="service-icon" role="img" aria-label="Icon of three beer taps" style="top:14px"></div>
    <div class="service-rule" style="top:3px;height:84px"></div>
    <h2 class="service-name">System<br>Design</h2>
    <ul class="service-points" style="top:14px">
      <li>Beverage Dispensing Design</li>
      <li>Bar walk-in cooler layout</li>
      <li>Designated Contact to work withyour team</li>
    </ul>
  </section>

  <section class="service" style="top:380px">
    <div class="service-icon" role="img" aria-label="Icon of a tap with two glasses" style="top:12px"></div>
    <div class="service-rule" style="top:3px;height:84px"></div>
    <h2 class="service-name">System<br>Installation</h2>
    <ul class="service-points" style="top:-4px">
      <li>Perfectly balanced dispense system</li>
      <li>Installed by certified Draft System Installers</li>
      <li>Superior Dispense Equipement</li>
      <li>304 grade stainless steel</li>
      <li>Glycon Chiller warranty :- 1 year for part and 3 years for compressor</li>
    </ul>
  </section>

  <section class="service" style="top:500px">
    <div class="service-icon" role="img" aria-label="Icon of a service technician with a wrench" style="top:10px"></div>
    <div class="service-rule" style="top:0;height:84px"></div>
    <h2 class="service-name">Maintenance<br>Services</h2>
    <ul class="service-points" style="top:5px">
      <li>Annual Glycol Chiller Maintenance</li>
      <li>Draft Beer Systems troubleshooting and evaluation</li>
      <li>Draftline bi-weekly maintenance</li>
      <li>Gas Blender and Gas Regulator Services and Repair</li>
    </ul>
  </section>

  <div class="tap-handles-photo" role="img" aria-label="Photo of a brass draft tower with a row of colorful tap handles"></div>

  <ul class="strengths">
    <li>System Experts</li>
    <li>Industry Leading Knowledge</li>
    <li>Excellent Service</li>
  </ul>

  <address class="contact">
    <div class="company">Tapline Pro</div>
    <div class="row"><svg viewBox="0 0 24 24"><path d="M6.6 10.8a15 15 0 0 0 6.6 6.6l2.2-2.2a1 1 0 0 1 1-.25 11.4 11.4 0 0 0 3.6.57 1 1 0 0 1 1 1V20a1 1 0 0 1-1 1A17 17 0 0 1 3 4a1 1 0 0 1 1-1h3.5a1 1 0 0 1 1 1c0 1.25.2 2.45.57 3.57a1 1 0 0 1-.25 1z"/></svg>555-014-2271</div>
    <div class="row"><svg viewBox="0 0 24 24"><path d="M12 2a10 10 0 1 0 0 20 10 10 0 0 0 0-20zm6.9 6h-3a15.6 15.6 0 0 0-1.4-3.6A8 8 0 0 1 18.9 8zM12 4a14 14 0 0 1 1.9 4h-3.8A14 14 0 0 1 12 4zM4.3 14a8 8 0 0 1 0-4h3.4a16 16 0 0 0 0 4zm.8 2h3a15.6 15.6 0 0 0 1.4 3.6A8 8 0 0 1 5.1 16zM8 8H5.1a8 8 0 0 1 4.3-3.6A15.6 15.6 0 0 0 8 8zm4 12a14 14 0 0 1-1.9-4h3.8A14 14 0 0 1 12 20zm2.3-6H9.7a14.7 14.7 0 0 1 0-4h4.6a14.7 14.7 0 0 1 0 4zm.3 5.6A15.6 15.6 0 0 0 16 16h3a8 8 0 0 1-4.4 3.6zm1.7-5.6a16 16 0 0 0 0-4h3.4a8 8 0 0 1 0 4z"/></svg>www.taplinepro.example</div>
    <div class="row"><svg viewBox="0 0 24 24"><path d="M2 5h20v14H2zm2 2v.5l8 5 8-5V7z"/></svg>P.O. Box 12, Millbrook, OH 40000</div>
  </address>
</main>
</body>
</html>
```